Brightmark Power website design

Electrical contractor in Perth that services the domestic and commercial markets. our services include but not limited to:

New Home Installations and Design
Commercial Shop Fit Outs
Rewires
Renovations
Switchboard Upgrades
Kitchen and Bathroom Renovations
RCD'S (Safety Switches)
Smoke Alarms
Power points
Security Lighting
Energy Efficient LED Lighting Designs
Garden Lighting
Downlights
General Electrical Maintenance
TV and Phone Points
Home Theatre Installs
Safety Certificates
24hr Call out service
Electric Hot Water Units
Credit cards accepted

www.sociabook.example/brightmarkpower

Contractor

5+ page

Sans Serif

acd037
fbee3e

• contact page, services page, about us, careers page, somewhere I can put some testimonials, somewhere potential clients can book our services online, on the homepage somewhere showing that we can provide 24/7 emergency service
• icon stating that we accept all major credit cards

```html
<!DOCTYPE html>
<html lang="en">
<head>
<meta charset="utf-8">
<title>Brightmark Power</title>
<link href="https://fonts.googleapis.com/css2?family=Ubuntu:wght@300;400;500;700&family=Open+Sans:wght@400;600;700&display=swap" rel="stylesheet">
<style>
:root{
  --lime:#e3e02e;
  --lime-dark:#c9cf2a;
  --navy:#0c4a86;
  --band:#1d5a93;
  --text:#5d5d5d;
  --muted:#8a8a8a;
  --faint:#dcdcdc;
  --panel:#f5f6f7;
  --card:#fafafa;
  --footer:#f1f1f1;
  --white:#ffffff;
}
*{margin:0;padding:0;box-sizing:border-box}
html,body{width:1050px;height:1200px;overflow:hidden;background:var(--white)}
body{position:relative;font-family:'Open Sans',sans-serif;color:var(--text)}
.abs{position:absolute}

/* header */
.site-header{position:absolute;left:0;top:0;width:1050px;height:139px;background:#f7f8f9}
.brand{position:absolute;left:152px;top:30px;display:flex;align-items:center;gap:12px}
.brand-dot{width:22px;height:22px;border-radius:50%;background:var(--lime)}
.brand-name{font-family:'Ubuntu',sans-serif;font-weight:500;font-size:29px;color:var(--navy);letter-spacing:.2px}
.brand-reg{position:absolute;left:359px;top:103px;font-size:7px;line-height:8px;color:var(--navy)}
.util-links{position:absolute;right:150px;top:23px;display:flex;align-items:center;gap:11px;font-family:'Ubuntu',sans-serif;font-weight:300;font-size:12.5px;color:#8a8a8a}
.util-links .sep{color:#aaa}
.util-links .cards{color:var(--lime-dark);display:flex;align-items:center;gap:6px}
.contact-row{position:absolute;right:150px;top:55px;display:flex;align-items:center;gap:16px}
.member-badge{width:74px;height:20px;background:#e3e6ea;border-radius:2px}
.phone{display:flex;align-items:center;gap:7px;font-family:'Ubuntu',sans-serif;font-size:19px;color:var(--navy)}
.main-nav{position:absolute;right:150px;top:89px;display:flex;gap:19px;font-family:'Ubuntu',sans-serif;font-weight:300;font-size:14.5px;color:#555}
.main-nav a{color:inherit;text-decoration:none;padding-bottom:3px}
.main-nav a.active{color:var(--lime-dark);border-bottom:2px solid var(--lime)}

/* hero */
.hero{position:absolute;left:0;top:139px;width:1050px;height:437px;background:radial-gradient(ellipse at 52% 45%,#3b60b0 0%,#1a3a86 30%,#0e2560 60%,#4a5a78 100%)}
.hero-photo{position:absolute;inset:0}
.hero-arrow{position:absolute;top:168px;width:44px;height:44px;border-radius:50%;background:rgba(220,220,220,.75)}
.hero-arrow.prev{left:57px}
.hero-arrow.next{right:56px}
.hero-title{position:absolute;left:0;width:1050px;top:325px;text-align:center;font-family:'Ubuntu',sans-serif;font-size:35px;color:var(--lime);letter-spacing:.5px}
.hero-text{position:absolute;left:235px;width:580px;top:368px;text-align:center;font-size:11.5px;line-height:14px;color:var(--white)}

/* welcome */
.welcome-title{position:absolute;left:150px;top:610px;font-family:'Ubuntu',sans-serif;font-size:36px;color:var(--navy)}
.welcome-copy{position:absolute;left:151px;top:656px;width:490px;font-size:10.6px;line-height:13px;color:#666}
.welcome-copy p+p{margin-top:11px}
.features{position:absolute;left:658px;top:617px;width:242px}
.feature{display:flex;align-items:center;gap:14px;height:43px;background:var(--panel);margin-bottom:4px;padding-left:12px;font-family:'Ubuntu',sans-serif;font-size:14px;line-height:14px;color:var(--navy)}
.feature svg{flex:none}

/* booking band */
.booking-band{position:absolute;left:0;top:777px;width:1050px;height:123px;background:var(--band)}
.booking-title{position:absolute;left:150px;top:45px;font-family:'Ubuntu',sans-serif;font-size:29px;color:var(--white)}
.booking-button{position:absolute;left:637px;top:38px;width:263px;height:47px;background:var(--white);border-radius:2px;font-family:'Ubuntu',sans-serif;font-size:22px;color:var(--navy);text-align:center;line-height:47px}

/* services */
.services-title{position:absolute;left:150px;top:927px;font-family:'Ubuntu',sans-serif;font-size:25px;color:var(--lime)}
.grid-toggle{position:absolute;left:881px;top:934px;width:19px;height:19px}
.services{position:absolute;left:150px;top:970px;display:flex;gap:8.5px}
.service{width:118px;height:148px;background:var(--card);display:flex;flex-direction:column;align-items:center;padding-top:28px;color:#e0e0e0}
.service.active{background:var(--panel);color:var(--navy)}
.service-name{margin-top:14px;text-align:center;font-size:9px;line-height:11px;font-weight:700;color:#dadada;text-transform:uppercase}
.service.active .service-name{color:var(--navy)}

/* footer */
.site-footer{position:absolute;left:0;top:1146px;width:1050px;height:54px;background:var(--footer);font-size:9px;color:#666}
.copyright{position:absolute;left:152px;top:21px}
.footer-nav{position:absolute;right:152px;top:21px;display:flex;gap:8px}
.footer-nav a{color:#666;text-decoration:none}
.footer-nav a.active{color:var(--lime-dark)}
</style>
</head>
<body>

<header class="site-header">
  <div class="brand"><span class="brand-dot"></span><span class="brand-name">Brightmark Power</span></div>
  <div class="brand-reg">EC 20417<br>ABN 40118226903</div>

  <div class="util-links">
    <span>LOGIN</span><span class="sep">|</span><span>REGISTER</span><span class="sep">|</span>
    <span class="cards">
      <svg width="24" height="16" viewBox="0 0 24 16"><rect x="1" y="2" width="20" height="13" rx="2" fill="none" stroke="#0c4a86" stroke-width="1.8"/><rect x="1" y="5" width="20" height="2.5" fill="#0c4a86"/><path d="M15 9l3 3 5-8" fill="none" stroke="#e3e02e" stroke-width="2"/></svg>
      WE ACCEPTS ALL MAJOR CREDIT CARDS
    </span>
  </div>

  <div class="contact-row">
    <span class="member-badge" aria-label="Member badge"></span>
    <span class="phone">
      <svg width="26" height="26" viewBox="0 0 26 26"><circle cx="13" cy="13" r="11" fill="none" stroke="#0c4a86" stroke-width="1.6"/><text x="13" y="16" text-anchor="middle" font-family="Ubuntu,sans-serif" font-size="8" font-weight="700" fill="#0c4a86">24/7</text></svg>
      10 20 30 40 50
    </span>
  </div>

  <nav class="main-nav">
    <a class="active" href="#">Home</a><a href="#">Services</a><a href="#">About Us</a><a href="#">Careers</a><a href="#">Testimonials</a><a href="#">Contact</a>
  </nav>
</header>

<section class="hero">
  <div class="hero-photo" role="img" aria-label="Photo of a glowing light bulb among hanging unlit bulbs on a blue background"></div>
  <span class="hero-arrow prev"><svg width="44" height="44" viewBox="0 0 44 44"><path d="M25 13l-9 9 9 9" fill="none" stroke="#555" stroke-width="1.6"/></svg></span>
  <span class="hero-arrow next"><svg width="44" height="44" viewBox="0 0 44 44"><path d="M19 13l9 9-9 9" fill="none" stroke="#555" stroke-width="1.6"/></svg></span>
  <h1 class="hero-title">BRIGHTMARK POWER</h1>
  <p class="hero-text">Lorem ipsum dolor sit amet, consectetuer adipiscing elit, sed diam nonummy nibh euismod tincidunt ut laoreet dolore magna aliquam erat volutpat. Ut wisi enim ad minim veniam, quis nostrud exerci tation ullamcorper suscipit lobortis nisl ut aliquip ex ea commodo consequat.</p>
</section>

<h2 class="welcome-title">WELCOME</h2>
<div class="welcome-copy">
  <p>Lorem ipsum dolor sit amet, consectetuer adipiscing elit, sed diam nonummy nibh euismod tincidunt ut laoreet dolore magna aliquam erat volutpat. Ut wisi enim ad minim veniam, quis nostrud exerci tation ullamcorper suscipit lobortis nisl ut aliquip ex ea commodo consequat.</p>
  <p>Duis autem vel eum iriure dolor in hendrerit in vulputate velit esse molestie consequat, vel illum dolore eu feugiat nulla facilisis at vero eros et accumsan et iusto odio dignissim qui blandit praesent luptatum zzril delenit augue duis dolore te feugait nulla facilisi.</p>
</div>

<div class="features">
  <div class="feature">
    <svg width="34" height="30" viewBox="0 0 34 30"><circle cx="17" cy="15" r="12" fill="none" stroke="#0c4a86" stroke-width="2"/><path d="M3 12l2 4 3-3" fill="none" stroke="#0c4a86" stroke-width="1.6"/><text x="17" y="18" text-anchor="middle" font-family="Ubuntu,sans-serif" font-size="9" font-weight="700" fill="#0c4a86">24/7</text></svg>
    <span>24/7 EMERGENCY<br>SERVICE</span>
  </div>
  <div class="feature">
    <svg width="34" height="30" viewBox="0 0 34 30"><rect x="3" y="7" width="24" height="16" rx="2" fill="none" stroke="#0c4a86" stroke-width="2"/><rect x="3" y="11" width="24" height="3" fill="#0c4a86"/><path d="M20 16l4 4 8-12" fill="none" stroke="#e3e02e" stroke-width="3"/></svg>
    <span>WE ACCEPT ALL MAJOR<br>CREDIT CARDS</span>
  </div>
  <div class="feature">
    <svg width="34" height="30" viewBox="0 0 34 30"><rect x="5" y="5" width="24" height="22" rx="1" fill="#0c4a86"/><rect x="10" y="2" width="3" height="6" fill="#0c4a86"/><rect x="21" y="2" width="3" height="6" fill="#0c4a86"/><g fill="#fff"><rect x="9" y="13" width="4" height="4"/><rect x="15" y="13" width="4" height="4"/><rect x="21" y="13" width="4" height="4"/><rect x="9" y="19" width="4" height="4"/><rect x="15" y="19" width="4" height="4"/><rect x="21" y="19" width="4" height="4"/></g></svg>
    <span>MAKE A CALL FOR<br>BOOKING</span>
  </div>
</div>

<section class="booking-band">
  <h2 class="booking-title">CONTACT US NOW FOR BOOKING!</h2>
  <a class="booking-button">CONTACT US</a>
</section>

<h2 class="services-title">SERVICES</h2>
<svg class="grid-toggle" viewBox="0 0 19 19"><rect x="0" y="0" width="9" height="9" fill="#e8e8e8"/><rect x="10" y="0" width="9" height="9" fill="#e3e02e"/><rect x="0" y="10" width="9" height="9" fill="#e8e8e8"/><rect x="10" y="10" width="9" height="9" fill="#e8e8e8"/></svg>

<div class="services">
  <div class="service">
    <svg width="54" height="54" viewBox="0 0 54 54" fill="none" stroke="currentColor" stroke-width="3"><path d="M8 26L27 8l19 18"/><path d="M13 22v20h28V22"/><rect x="22" y="30" width="9" height="12"/><path d="M14 46c6 4 16 4 24 0h8"/></svg>
    <div class="service-name">New Home<br>Installations<br>and Design</div>
  </div>
  <div class="service active">
    <svg width="54" height="54" viewBox="0 0 54 54"><path d="M8 8h38l4 12H4z" fill="currentColor"/><path d="M8 22h38v24H8z" fill="currentColor"/><rect x="13" y="27" width="12" height="19" fill="#f5f6f7"/><rect x="29" y="27" width="12" height="10" fill="#f5f6f7"/></svg>
    <div class="service-name">Commercial<br>Shop Fit Outs</div>
  </div>
  <div class="service">
    <svg width="54" height="54" viewBox="0 0 54 54" fill="none" stroke="currentColor" stroke-width="3"><rect x="5" y="5" width="44" height="44" rx="4"/><path d="M5 27h12M37 27h12"/><path d="M17 19h10a8 8 0 010 16H17z"/><path d="M12 23h5M12 31h5"/></svg>
    <div class="service-name">Rewires</div>
  </div>
  <div class="service">
    <svg width="54" height="54" viewBox="0 0 54 54" fill="none" stroke="currentColor" stroke-width="3"><circle cx="27" cy="27" r="21"/><path d="M20 24a7 7 0 1114 0c0 4-3 5-3 9h-8c0-4-3-5-3-9z"/><path d="M23 37h8M24 41h6"/></svg>
    <div class="service-name">Renovations</div>
  </div>
  <div class="service">
    <svg width="54" height="54" viewBox="0 0 54 54" fill="none" stroke="currentColor" stroke-width="3"><rect x="6" y="6" width="42" height="12"/><rect x="6" y="21" width="42" height="12"/><path d="M12 36v10M42 36v10M6 46h42"/><circle cx="40" cy="12" r="1.5"/><circle cx="40" cy="27" r="1.5"/></svg>
    <div class="service-name">Switchboard<br>Upgrades</div>
  </div>
  <div class="service">
    <svg width="78" height="54" viewBox="0 0 78 54" fill="none" stroke="currentColor" stroke-width="3"><path d="M4 46V26h52v20z"/><path d="M58 46V8h16v38z"/><path d="M30 26V14M24 14h12M14 8v10M10 18h8"/><rect x="10" y="31" width="12" height="10"/><path d="M28 36h22"/></svg>
    <div class="service-name">Kitchen and<br>Bathroom<br>Renovations</div>
  </div>
</div>

<footer class="site-footer">
  <div class="copyright">© 2014 Brightmark Power. All Rights Reserved.</div>
  <nav class="footer-nav">
    <a class="active" href="#">Home</a><a href="#">Services</a><a href="#">About Us</a><a href="#">Careers</a><a href="#">Testimonials</a><a href="#">Contact</a>
  </nav>
</footer>

</body>
</html>
```